New nutrition counseling business needs a flyer and logo design for marketing purposes

Need a new flyer for distribution to advertise and inform the public about new Dietetic Counseling service. The new business name is Harbor of Vitality with “Harbor” being the main name. It will provide nutrition consultation services to individuals who seek to change their dietary habits to achieve a variety of different health objectives. These objectives can include, but are not limited to weight management, enhanced athletic performance, improved health biomarkers, and reducing the risks or symptoms of chronic nutrition related diseases. The services provided include direct one on one counseling that entails health and nutrition assessments, evaluation of goals, and the determination of strategies to meet these goals. We would like to see designs that use an ocean color scheme with purple aspects as well. Color and logo ideas attached in uploads. Please include logo on the flyer as well.

Target Market(s)

General Population

Colors
0094D4
00A9DD
6FCCEA
C7EBF8
E9F6FB
00AB8E
00BBA5
67D7C9
C6EFE9
E9F9F6
6B429C
8869AF
B7A5CE
E3DAEB
F3F0F8

Requirements
Nice to have
• Pictures of nourishing foods, fruits, vegetables etc.
Should not have
• Do not include people in flyer or logo design

```html
<!DOCTYPE html>
<html lang="en">
<head>
<meta charset="utf-8">
<title>Harbor of Vitality – Nutrition Counseling Flyer</title>
<link href="https://fonts.googleapis.com/css2?family=Bebas+Neue&family=Oswald:wght@500;600;700&family=Poppins:wght@400;500;600;700;800&family=Montserrat:wght@600;700;800&display=swap" rel="stylesheet">
<style>
:root{
  --page:#ffffff;
  --paper:#efefef;
  --blue:#1d6ab3;
  --navy:#1b3f66;
  --navy-deep:#14335a;
  --band-light:#3a6c9c;
  --green:#7dc242;
  --green-soft:#a5cd72;
  --teal:#19c1a6;
  --ink:#1f1f1f;
  --white:#ffffff;
}
*{margin:0;padding:0;box-sizing:border-box}
html,body{width:1093px;height:1200px;overflow:hidden;background:var(--page)}
.flyer{position:absolute;left:106px;top:30px;width:880px;height:1140px;background:var(--paper);overflow:hidden;font-family:"Poppins",sans-serif;color:var(--ink)}

.brand{position:absolute;left:42px;top:78px;display:flex;align-items:center;gap:12px}
.brand-dot{width:18px;height:18px;border-radius:50%;background:var(--teal)}
.brand-name{font-family:"Poppins",sans-serif;font-weight:700;font-size:34px;line-height:1.05;color:var(--blue)}

.headline{position:absolute;left:37px;top:256px;width:340px}
.headline span{display:block;white-space:nowrap}
.headline .line-lead{font-family:"Bebas Neue",sans-serif;font-weight:400;font-size:43px;line-height:44px;color:var(--ink)}
.headline .line-focus{font-family:"Bebas Neue",sans-serif;font-weight:400;font-size:55px;line-height:52px;color:var(--blue)}
.headline .line-big{font-family:"Poppins",sans-serif;font-weight:800;font-size:51px;line-height:56px;color:var(--blue);letter-spacing:-1px}
.headline .line-tag{font-family:"Poppins",sans-serif;font-weight:700;font-size:21px;line-height:32px;color:var(--green)}

.food-art{position:absolute;left:0;top:0}

.band{position:absolute;left:0;top:466px;width:880px;height:190px;background:linear-gradient(90deg,var(--navy) 0%,var(--band-light) 55%,var(--navy) 100%)}
.practitioner{position:absolute;left:41px;top:488px;color:var(--white);white-space:nowrap}
.practitioner .name{font-family:"Montserrat",sans-serif;font-weight:800;font-size:40px}
.practitioner .creds{font-family:"Poppins",sans-serif;font-weight:400;font-size:29px}
.license{position:absolute;left:39px;top:542px;height:33px;display:flex;font-family:"Montserrat",sans-serif;white-space:nowrap}
.license .label{background:var(--green);color:var(--white);font-weight:700;font-size:16px;letter-spacing:1.2px;padding-left:11px;display:flex;align-items:center;width:212px}
.license .value{background:var(--white);color:var(--ink);font-weight:800;font-size:22px;letter-spacing:2px;padding-left:13px;display:flex;align-items:center;width:153px}

.services-tab{position:absolute;left:0;top:616px}
.services-title{position:absolute;left:37px;top:616px;height:40px;line-height:42px;color:var(--white);font-weight:600;font-size:26px;white-space:nowrap}

.services{position:absolute;left:37px;top:672px;width:420px;list-style:none}
.services li{position:relative;padding-left:25px;font-size:17.5px;line-height:20.7px;margin-bottom:13.5px;color:var(--ink)}
.services li svg{position:absolute;left:0;top:4px}

.modes{position:absolute;left:494px;top:616px;width:333px;height:111px;background:var(--green-soft);border:5px solid var(--green);border-radius:11px;padding:6px}
.modes-inner{width:100%;height:100%;border:1.5px dashed var(--white);border-radius:6px;text-align:center;padding-top:16px;white-space:nowrap}
.modes .primary{font-family:"Bebas Neue",sans-serif;font-weight:400;font-size:30px;line-height:30px;color:var(--ink)}
.modes .secondary{font-family:"Poppins",sans-serif;font-weight:500;font-size:14.5px;letter-spacing:.8px;color:var(--white);line-height:24px}

.chat{position:absolute;left:496px;top:738px;width:323px;height:228px}
.chat svg{position:absolute;left:0;top:0}
.chat-title{position:absolute;left:40px;top:20px;font-family:"Oswald",sans-serif;font-weight:700;font-size:44px;color:var(--white);transform:rotate(-5deg) skewX(-8deg);transform-origin:left bottom;letter-spacing:1px;white-space:nowrap}
.chat-free{position:absolute;left:26px;top:96px;font-family:"Oswald",sans-serif;font-weight:700;font-size:45px;line-height:46px;color:var(--green)}
.chat-length{position:absolute;left:26px;top:142px;font-family:"Oswald",sans-serif;font-weight:600;font-size:27px;line-height:30px;color:var(--white)}
.chat-divider{position:absolute;left:145px;top:106px;width:2px;height:64px;background:var(--white)}
.chat-detail{position:absolute;left:160px;top:104px;width:130px;color:var(--white);font-size:13px;font-weight:600;line-height:14.5px}
.chat-detail strong{display:block;font-family:"Oswald",sans-serif;font-weight:600;font-size:19px;line-height:24px;color:var(--green);white-space:nowrap}

.contact{position:absolute;left:38px;top:1002px;width:798px;height:40px;border-radius:20px;background:#2d5f8e;display:flex;align-items:center;overflow:hidden;white-space:nowrap}
.contact .label{width:237px;text-align:center;font-family:"Montserrat",sans-serif;font-weight:800;font-size:26px;letter-spacing:3px;color:var(--green)}
.contact .phone{width:251px;height:100%;background:var(--navy-deep);border-left:2px solid var(--white);border-right:2px solid var(--white);display:flex;align-items:center;justify-content:center;gap:8px;font-family:"Poppins",sans-serif;font-weight:700;font-size:25px;color:var(--white)}
.contact .email{flex:1;display:flex;align-items:center;justify-content:center;gap:10px;font-family:"Poppins",sans-serif;font-weight:500;font-size:20px;color:var(--white)}

.food-strip{position:absolute;left:0;top:1056px;width:880px;height:84px;background:linear-gradient(90deg,#b58e5a 0%,#c0394a 20%,#e9e5dd 40%,#9a6a45 52%,#e9e5dd 64%,#c0394a 82%,#b58e5a 100%)}
</style>
</head>
<body>
<main class="flyer">

  <div class="brand">
    <span class="brand-dot"></span>
    <span class="brand-name">Harbor<br>of Vitality</span>
  </div>

  <div class="band"></div>

  <svg class="food-art" width="880" height="700" viewBox="0 0 880 700">
    <defs>
      <radialGradient id="salad-tone" cx="50%" cy="50%" r="50%">
        <stop offset="0%" stop-color="#c9a24a"/>
        <stop offset="55%" stop-color="#5f9a32"/>
        <stop offset="100%" stop-color="#2f6b28"/>
      </radialGradient>
      <radialGradient id="plate-tone" cx="50%" cy="50%" r="50%">
        <stop offset="0%" stop-color="#e07d5c"/>
        <stop offset="45%" stop-color="#6ca13a"/>
        <stop offset="100%" stop-color="#f4f4f2"/>
      </radialGradient>
      <radialGradient id="fruit-tone" cx="50%" cy="50%" r="50%">
        <stop offset="0%" stop-color="#f3c63a"/>
        <stop offset="55%" stop-color="#f08a2a"/>
        <stop offset="100%" stop-color="#d8283a"/>
      </radialGradient>
    </defs>
    <circle cx="760" cy="164" r="172" fill="none" stroke="var(--teal)" stroke-width="6"/>
    <circle cx="745" cy="168" r="166" fill="url(#salad-tone)" role="img" aria-label="Bowl of mixed salad greens, mushrooms, chickpeas and quinoa"/>
    <circle cx="544" cy="276" r="150" fill="var(--green)"/>
    <circle cx="552" cy="276" r="140" fill="#4a8fd6"/>
    <circle cx="552" cy="282" r="132" fill="url(#plate-tone)" role="img" aria-label="Plate of baked salmon with asparagus and cherry tomatoes"/>
    <circle cx="722" cy="422" r="140" fill="var(--green)"/>
    <circle cx="728" cy="414" r="132" fill="var(--teal)"/>
    <circle cx="722" cy="414" r="126" fill="url(#fruit-tone)" role="img" aria-label="Bowl of fresh fruit with kiwi, mango, oranges, strawberries and grapes"/>
  </svg>

  <h1 class="headline">
    <span class="line-lead">HELPING CLIENTS FOSTER</span>
    <span class="line-focus">POSITIVE NUTRITION</span>
    <span class="line-big">PRACTICES</span>
    <span class="line-tag">FOR A HEALTHIER LIFESTYLE</span>
  </h1>

  <div class="practitioner"><span class="name">Marisol Delgado,</span><span class="creds">MS, RD, LD/N</span></div>
  <div class="license"><span class="label">LICENSE NUMBER</span><span class="value">ND 20471</span></div>

  <svg class="services-tab" width="380" height="40" viewBox="0 0 380 40">
    <polygon points="0,0 318,0 351,40 0,40" fill="var(--green)"/>
    <polygon points="326,0 338,0 371,40 359,40" fill="var(--white)"/>
    <polygon points="344,0 354,0 380,32 380,40 377,40" fill="var(--white)"/>
  </svg>
  <h2 class="services-title">SERVICES OFFERED</h2>

  <ul class="services">
    <li><svg width="13" height="13" viewBox="0 0 13 13"><rect x="1" y="2" width="10" height="10" rx="2" fill="none" stroke="var(--blue)" stroke-width="1.4"/><path d="M3.5 6.5l2.5 2.5 6-7" fill="none" stroke="var(--blue)" stroke-width="1.6"/></svg>Medical Nutrition Therapy for chronic conditions such as diabetes, hypertension, high cholesterol, and more</li>
    <li><svg width="13" height="13" viewBox="0 0 13 13"><rect x="1" y="2" width="10" height="10" rx="2" fill="none" stroke="var(--blue)" stroke-width="1.4"/><path d="M3.5 6.5l2.5 2.5 6-7" fill="none" stroke="var(--blue)" stroke-width="1.6"/></svg>Weight Management</li>
    <li><svg width="13" height="13" viewBox="0 0 13 13"><rect x="1" y="2" width="10" height="10" rx="2" fill="none" stroke="var(--blue)" stroke-width="1.4"/><path d="M3.5 6.5l2.5 2.5 6-7" fill="none" stroke="var(--blue)" stroke-width="1.6"/></svg>Healthy Eating and Meal Planning</li>
    <li><svg width="13" height="13" viewBox="0 0 13 13"><rect x="1" y="2" width="10" height="10" rx="2" fill="none" stroke="var(--blue)" stroke-width="1.4"/><path d="M3.5 6.5l2.5 2.5 6-7" fill="none" stroke="var(--blue)" stroke-width="1.6"/></svg>Nutrition for Athletic Performance</li>
    <li><svg width="13" height="13" viewBox="0 0 13 13"><rect x="1" y="2" width="10" height="10" rx="2" fill="none" stroke="var(--blue)" stroke-width="1.4"/><path d="M3.5 6.5l2.5 2.5 6-7" fill="none" stroke="var(--blue)" stroke-width="1.6"/></svg>Pre and Post Natal Nutrition</li>
    <li><svg width="13" height="13" viewBox="0 0 13 13"><rect x="1" y="2" width="10" height="10" rx="2" fill="none" stroke="var(--blue)" stroke-width="1.4"/><path d="M3.5 6.5l2.5 2.5 6-7" fill="none" stroke="var(--blue)" stroke-width="1.6"/></svg>Personalized meal plans uniquely catered to each individual</li>
    <li><svg width="13" height="13" viewBox="0 0 13 13"><rect x="1" y="2" width="10" height="10" rx="2" fill="none" stroke="var(--blue)" stroke-width="1.4"/><path d="M3.5 6.5l2.5 2.5 6-7" fill="none" stroke="var(--blue)" stroke-width="1.6"/></svg>Highly collaborative approach to help you meet your goals</li>
  </ul>

  <aside class="modes">
    <div class="modes-inner">
      <p class="primary">BOTH IN PERSON AND VIRTUAL</p>
      <p class="secondary">CONSULTATIONS ARE OFFERED</p>
    </div>
  </aside>

  <section class="chat">
    <svg width="323" height="228" viewBox="0 0 323 228">
      <polygon points="22,34 316,0 323,6 323,90 14,100" fill="#2e5d8c"/>
      <path d="M14,95 L323,83 L323,180 Q323,188 315,188 L60,188 L32,228 L38,188 L8,188 Q0,188 1,180 Z" fill="var(--navy-deep)"/>
    </svg>
    <p class="chat-title">LET'S CHAT!</p>
    <p class="chat-free">FREE</p>
    <p class="chat-length">15-MINUTE</p>
    <span class="chat-divider"></span>
    <p class="chat-detail">Introductory consultation to discuss program<strong>DETAILS AND RATES</strong></p>
  </section>

  <footer class="contact">
    <span class="label">CONTACT</span>
    <span class="phone">
      <svg width="20" height="20" viewBox="0 0 20 20"><circle cx="10" cy="10" r="10" fill="var(--green)"/><path d="M6.5 5.2l2 -.4 1.1 2.6-1.3 1c.6 1.3 1.6 2.3 2.9 2.9l1-1.3 2.6 1.1-.4 2c-4.4.2-8.1-3.5-7.9-7.9z" fill="var(--white)"/></svg>
      555-014-2287
    </span>
    <span class="email">
      <svg width="20" height="20" viewBox="0 0 20 20"><circle cx="10" cy="10" r="10" fill="var(--green)"/><rect x="5" y="6.5" width="10" height="7" rx="1" fill="none" stroke="var(--navy-deep)" stroke-width="1.3"/><path d="M5.5 7l4.5 3.6L14.5 7" fill="none" stroke="var(--navy-deep)" stroke-width="1.3"/></svg>
      Marisol@delgadord.net
    </span>
  </footer>

  <div class="food-strip" role="img" aria-label="Bowls of granola, raspberries, hazelnuts and blueberries on a light table"></div>
</main>
</body>
</html>
```